Business card design for sustainable building and development company

Need a business card design for a new sustainable building and real estate development company in the San Francisco Bay area. Name of company is "Norvale Advisors, LLC" and we provide "Sustainable building, energy and development services" for residential and non residential projects. We'd like the following colors used but not all area required: green, gray, blue. Design should communicate innovation, professionalism and sustainability. Our current website is www.norvale-advisors.example. Another possible design idea is to have the following listed on the back of the card:
Certified: TRAM QX, Leaf Mark Grader, VOLT Grader, EcoState Examiner, RDQ HX Building Analyst. Its not a must but could be text that could be used for back of card. Overall, we are open to a simple, clean design and or one with more text than usual for a card.

Industry/Entity Type

Real Estate

Contact Information for Business Card

Name on card: Dmitri L. Hasby
Title for Name: Principal + Founder
Phone: 555.418.2096
Email: dhasby@norvale-advisors.example
Website: www.norvale-advisors.example

Also, please add the following for address:
San Francisco, California

Requirements
Nice to have
• If you can integrate the outline of a skyline on the backside of the card and if it looks good, I would like to see the design
Should not have
• a barcode;

```html
<!DOCTYPE html>
<html lang="en">
<head>
<meta charset="utf-8">
<title>Norvale Advisors — Business Card</title>
<link href="https://fonts.googleapis.com/css2?family=Open+Sans:wght@300;400;600;700;800&display=swap" rel="stylesheet">
<style>
  :root {
    --bg: #e9e7e2;
    --paper: #ffffff;
    --green: #5cb63b;
    --green-dark: #3f9a26;
    --green-light: #9fd47f;
    --green-pale: #e3f2d8;
    --gray: #7a7a7a;
    --white: #ffffff;
  }
  * { margin: 0; padding: 0; box-sizing: border-box; }
  html, body {
    width: 1200px; height: 1023px; overflow: hidden;
    background: var(--bg);
    font-family: "Open Sans", Arial, sans-serif;
  }
  .sheet {
    position: relative; width: 1200px; height: 1023px;
    display: flex; flex-direction: column; align-items: center; justify-content: center; gap: 36px;
  }
  .card {
    position: relative; width: 800px; height: 457px; overflow: hidden;
    box-shadow: 0 6px 18px rgba(0,0,0,.18);
  }

  /* Front */
  .card--front { background: var(--paper); }
  .front__ring {
    position: absolute; right: 40px; top: -150px; width: 340px; height: 340px;
    border-radius: 50%; border: 34px solid var(--green-pale);
  }
  .brand { position: absolute; left: 44px; top: 60px; display: flex; align-items: center; gap: 14px; }
  .brand__dot { width: 64px; height: 64px; border-radius: 50%; background: var(--green-light); flex: none; }
  .brand__name { font-weight: 700; font-size: 38px; line-height: 1; color: var(--green); letter-spacing: -0.5px; }
  .brand__tagline { margin-top: 5px; font-size: 9.5px; font-weight: 600; color: var(--gray); letter-spacing: .6px; text-transform: uppercase; }

  .person { position: absolute; left: 52px; top: 200px; }
  .person__name { font-size: 30px; font-weight: 400; color: var(--green); }
  .person__title { font-size: 19px; color: var(--gray); margin-top: 2px; }

  .contacts { position: absolute; left: 52px; top: 286px; list-style: none; }
  .contacts__item { display: flex; align-items: center; gap: 12px; font-size: 19px; color: var(--green); line-height: 30px; }
  .contacts__icon { width: 16px; height: 16px; flex: none; }

  .front__band { position: absolute; left: 0; bottom: 0; width: 800px; height: 120px; }
  .front__city { position: absolute; right: 44px; bottom: 22px; font-size: 21px; color: var(--white); }

  /* Back */
  .card--back { background: linear-gradient(135deg, var(--green-light) 0%, var(--green) 45%, var(--green-dark) 100%); }
  .back__brand { position: absolute; left: 70px; top: 130px; display: flex; align-items: center; gap: 20px; }
  .back__dot { width: 120px; height: 120px; border-radius: 50%; background: var(--white); flex: none; }
  .back__name { font-size: 54px; font-weight: 800; color: var(--white); line-height: 1; letter-spacing: -0.5px; }
  .back__tagline { margin-top: 8px; font-size: 13.5px; color: var(--white); letter-spacing: .9px; text-transform: uppercase; }
  .back__web { position: absolute; left: 70px; bottom: 44px; font-size: 22px; color: var(--white); }
</style>
</head>
<body>
<main class="sheet">

  <section class="card card--front" aria-label="Card front">
    <div class="front__ring"></div>

    <div class="brand">
      <span class="brand__dot"></span>
      <div>
        <div class="brand__name">Norvale Advisors</div>
        <div class="brand__tagline">Sustainable building, energy &amp; development services</div>
      </div>
    </div>

    <div class="person">
      <div class="person__name">Dmitri L. Hasby</div>
      <div class="person__title">Principal/Owner</div>
    </div>

    <ul class="contacts">
      <li class="contacts__item">
        <svg class="contacts__icon" viewBox="0 0 16 16"><rect x="1" y="1" width="14" height="14" rx="2" fill="#5cb63b"/><path d="M5 4h2l1 2.5-1.2 1a6 6 0 0 0 2.7 2.7l1-1.2 2.5 1v2a1 1 0 0 1-1 1A9 9 0 0 1 4 5a1 1 0 0 1 1-1z" fill="#fff"/></svg>
        555.418.2096
      </li>
      <li class="contacts__item">
        <svg class="contacts__icon" viewBox="0 0 16 16"><rect x="1" y="1" width="14" height="14" rx="2" fill="#5cb63b"/><path d="M3.5 5h9v6.5h-9z M3.5 5l4.5 3.6L12.5 5" fill="none" stroke="#fff" stroke-width="1.2"/></svg>
        dhasby@norvale-advisors.example
      </li>
      <li class="contacts__item">
        <svg class="contacts__icon" viewBox="0 0 16 16"><rect x="1.5" y="1.5" width="13" height="13" rx="2" fill="none" stroke="#5cb63b" stroke-width="1.4"/></svg>
        www.norvale-advisors.example
      </li>
    </ul>

    <svg class="front__band" viewBox="0 0 800 120" preserveAspectRatio="none" aria-hidden="true">
      <defs>
        <linearGradient id="bandFade" x1="0" y1="0" x2="1" y2="0">
          <stop offset="0" stop-color="#e3f2d8"/>
          <stop offset="0.5" stop-color="#9fd47f"/>
          <stop offset="1" stop-color="#5cb63b"/>
        </linearGradient>
      </defs>
      <path d="M0 90 C220 60 480 40 800 10 L800 120 L0 120 Z" fill="url(#bandFade)" opacity=".6"/>
      <path d="M0 110 C260 90 520 70 800 52 L800 120 L0 120 Z" fill="url(#bandFade)"/>
    </svg>
    <div class="front__city">San Francisco, California</div>
  </section>

  <section class="card card--back" aria-label="Card back">
    <div class="back__brand">
      <span class="back__dot"></span>
      <div>
        <div class="back__name">Norvale Advisors</div>
        <div class="back__tagline">Sustainable building, energy &amp; development services</div>
      </div>
    </div>
    <div class="back__web">norvale-advisors.example</div>
  </section>

</main>
</body>
</html>
```